Loomvista: fashion design product software needs your help

Fashion design product software company requests your assistance in designing a complete stationary package around our new logo design. Our software assists fashion designers and apparel houses with efficient communication and streamlined production between each other and manufacturers throughout the entire project design life cycle.

The look should reflect clean, simple and modern design. Not too "techie." Must use the provided logo and colors (or variations on the chosen colors, i.e. percentages as needed).

Reference website: www.loomvista-example.com

Buzzwords: manufacturing, production, apparel design/ers, streamlined process, effective communication, business, production software.

Please try to tone down or make the colors more subtle with more simple design style, layout. No sewing  theme. Thank you.

Target Market(s)

fashion designers and apparel houses that use software to manage and track production process life cycle.

Industry/Entity Type

Communication

Requirements
Must have
• Use of the logo and colors-or variations of colors (attached)
Nice to have
• Playfulness but corporate: with a sense of practicality, economical, streamlined production. Embossing considered.
Should not have
• Please keep in mind economics both financially and economically. Save trees and money! We believe in tactile paper but not "fashion-y" or sparkly, over-the-top colors, effects or production.

```html
<!DOCTYPE html>
<html lang="en">
<head>
<meta charset="utf-8">
<title>Loomvista Stationery Set</title>
<link rel="stylesheet" href="https://fonts.googleapis.com/css2?family=Arimo:wght@400;700&display=swap">
<style>
  :root {
    --backdrop: #a7a7a7;
    --paper: #ffffff;
    --sky: #29abe2;
    --chestnut: #6b2d1b;
    --ink: #222222;
    --mist: #eef1f3;
    --window: #a9a9a9;
    --violet: #4d3a86;
    --stamp: #5a4a9c;
  }
  * { box-sizing: border-box; margin: 0; padding: 0; }
  html, body { width: 1200px; height: 900px; overflow: hidden; }
  body { background: var(--backdrop); font-family: "Arimo", Arial, sans-serif; }
  .stage { position: relative; width: 1200px; height: 900px; overflow: hidden; }

  .brand { display: inline-flex; align-items: center; gap: 6px; font-weight: 700; color: var(--chestnut); letter-spacing: -0.5px; line-height: 1; }
  .brand__dot { display: inline-block; border-radius: 50%; background: var(--sky); }

  /* Letterhead */
  .letterhead { position: absolute; left: 426px; top: 36px; width: 520px; height: 808px; background: var(--paper); }
  .letterhead__band { position: absolute; left: 0; top: 0; width: 100%; height: 12px; background: var(--sky); }
  .letterhead__header { position: absolute; left: 28px; top: 24px; width: 478px; height: 92px; background: var(--mist); border-radius: 6px; }
  .letterhead__header .brand { position: absolute; left: 32px; top: 26px; font-size: 28px; }
  .letterhead__header .brand__dot { width: 9px; height: 9px; }
  .letterhead__tag { position: absolute; right: 34px; top: 48px; font-size: 12px; color: var(--sky); }
  .letterhead__strap { position: absolute; left: 32px; top: 76px; font-size: 8px; color: var(--sky); }
  .letterhead__body { position: absolute; left: 54px; right: 46px; top: 204px; }
  .letterhead__title { font-size: 16px; font-weight: 700; color: var(--ink); margin-bottom: 14px; }
  .letterhead__body p { font-size: 9px; line-height: 12.5px; color: var(--ink); text-align: justify; margin-bottom: 12px; }
  .letterhead__signature { position: absolute; left: 296px; top: 660px; width: 110px; height: 56px; border-radius: 28px; background: linear-gradient(90deg, #d9d4ea, #c4bbe0); }
  .letterhead__seal { position: absolute; left: 404px; top: 636px; width: 88px; height: 88px; border-radius: 50%; border: 3px solid var(--stamp); opacity: 0.8; }
  .letterhead__footer { position: absolute; left: 28px; top: 770px; width: 478px; height: 20px; background: var(--mist); border-radius: 4px; }
  .letterhead__base { position: absolute; left: 156px; right: 0; bottom: 0; height: 8px; background: var(--chestnut); }

  /* Disc */
  .disc { position: absolute; left: 826px; top: 196px; width: 260px; height: 260px; border-radius: 50%;
    background: radial-gradient(circle at 50% 50%, #ffffff 0 15px, #bdbdbd 16px 40px, #e6e6e6 41px 60%, #cfcfcf 80%, #b8b8b8 100%);
    border: 1px solid #9d9d9d; }
  .disc__label { position: absolute; left: 42px; top: 44px; width: 82px; height: 64px; background: var(--paper); transform: rotate(-22deg); display: flex; align-items: center; justify-content: center; }
  .disc__label .brand { font-size: 14px; }
  .disc__label .brand__dot { width: 5px; height: 5px; }
  .disc__tag { position: absolute; left: 128px; top: 186px; font-size: 11px; color: var(--sky); transform: rotate(-28deg); white-space: nowrap; }

  /* Business cards */
  .card { position: absolute; background: var(--paper); }
  .card--back { left: 202px; top: 196px; width: 250px; height: 146px; transform: rotate(-12deg); }
  .card--back .card__base { position: absolute; left: 60px; right: 0; bottom: 0; height: 12px; background: var(--chestnut); }
  .card--front { left: 218px; top: 124px; width: 240px; height: 140px; transform: rotate(-2deg); border: 1px solid #d8d8d8; }
  .card--front .brand { position: absolute; left: 22px; top: 36px; font-size: 22px; }
  .card--front .brand__dot { width: 7px; height: 7px; }
  .card__name { position: absolute; right: 16px; top: 98px; font-size: 11px; color: var(--violet); }
  .card__rule { position: absolute; right: 16px; top: 114px; width: 86px; height: 1px; background: var(--violet); }

  /* Envelope */
  .envelope { position: absolute; left: 80px; top: 340px; width: 520px; height: 490px; background: var(--paper); transform: rotate(-7deg); }
  .envelope__band { position: absolute; left: 0; top: 0; width: 100%; height: 14px; background: var(--sky); }
  .envelope .brand { position: absolute; left: 96px; top: 60px; font-size: 36px; }
  .envelope .brand__dot { width: 11px; height: 11px; }
  .envelope__sender { position: absolute; left: 70px; top: 220px; font-size: 9px; line-height: 13px; color: var(--sky); }
  .envelope__window { position: absolute; left: 364px; top: 346px; width: 130px; height: 96px; background: var(--window); border-radius: 16px; }
  .envelope__base { position: absolute; left: 160px; right: 0; bottom: 0; height: 10px; background: var(--chestnut); }
</style>
</head>
<body>
<main class="stage">

  <section class="letterhead">
    <div class="letterhead__band"></div>
    <header class="letterhead__header">
      <span class="brand"><span class="brand__dot"></span>Loomvista</span>
      <span class="letterhead__tag">SAMPLE TEXT HERE</span>
      <span class="letterhead__strap">Production planning software for apparel designers and manufacturing teams worldwide.</span>
    </header>
    <article class="letterhead__body">
      <h1 class="letterhead__title">SAMPLE TEXT HERE</h1>
      <p>Thank you for your interest in our production platform. This letter summarises how our tools help design teams share specifications, track samples and keep every supplier informed from the first sketch to the final shipment. Each stage of the project life cycle lives in one shared workspace, so approvals move quickly and nothing is lost between studio, office and factory floor.</p>
      <p>In daily use, our clients report shorter sampling rounds and clearer conversations with their manufacturing partners. Tech packs, size charts and material notes update in real time, and every change is recorded with its author and date. Production managers see open tasks at a glance, while designers stay focused on the collection rather than on chasing email threads.</p>
      <p>We would be glad to arrange a short demonstration for your team at a time that suits you. Our onboarding specialists will import your current styles, set up supplier accounts and walk you through reporting, costing and delivery tracking. Most houses are working comfortably within two weeks, with support available whenever questions come up during a busy season.</p>
      <p>Please find our current service overview enclosed with this letter. If you have any questions about pricing, integrations or training, simply reply to this letter or contact our office directly. We look forward to supporting your next collection and to building a long and productive partnership together.</p>
    </article>
    <div class="letterhead__signature" role="img" aria-label="Handwritten signature"></div>
    <div class="letterhead__seal" role="img" aria-label="Company seal"></div>
    <div class="letterhead__footer"></div>
    <div class="letterhead__base"></div>
  </section>

  <section class="disc">
    <div class="disc__label"><span class="brand"><span class="brand__dot"></span>Loomvista</span></div>
    <span class="disc__tag">SAMPLE TEXT HERE</span>
  </section>

  <section class="card card--back"><div class="card__base"></div></section>
  <section class="card card--front">
    <span class="brand"><span class="brand__dot"></span>Loomvista</span>
    <span class="card__name">Name Surname</span>
    <span class="card__rule"></span>
  </section>

  <section class="envelope">
    <div class="envelope__band"></div>
    <span class="brand"><span class="brand__dot"></span>Loomvista</span>
    <address class="envelope__sender" style="font-style: normal;">
      Production software for apparel teams<br>
      Design, sampling and delivery in one place<br>
      Clear communication from studio to factory
    </address>
    <div class="envelope__window"></div>
    <div class="envelope__base"></div>
  </section>

</main>
</body>
</html>
```